Hush And Look Through Poster for Harbourline Stack Keepers

Task Description
I am the Vice President of Advocacy for the Harbourline Stack Keepers Association. I am looking to have a set of posters made for HALT (Hush And Look Through) in October. HALT is a time when all school children in BC are encouraged to Hush And Look Through for 15-20 minutes at some point in their day.

I would like to get a set of 2 digital posters designed (if possible it would be nice to have the option to print to both 11x17 and 8.5x 11 paper). We need a poster that is high school (Grade 8-12) appropriate and one that is elementary (Grade k-7) appropriate. Both posters need to be replicated in French. All posters need to have the KEU logo on them as well as the Harbourline Stack Keepers Association Logo.

My budget is not huge (whose is?), but we are flexible and open with design. We want posters that appeal to the age groups they are designed for and that promote reading. We would require the digital copy by August 20. Schools will arrange for their own printing as distribution to all the schools in BC is laborious.

Each poster needs to have the following information:

-Hush And Look Through (HALT)
- A Blank Spot that we can add a date to
-the logo for the KEU (attached)
-the logo for the HSKA (attached)- the logos do not have to be large.

Industry/Entity Type

Teacher

Font styles to use
Serif

Requirements
Must have
• -Hush And Look Through (HALT)
• - A Blank Spot that we can add a date to
• -the logo for the KEU (attached)
• -the logo for the HSKA (attached)- the logos do not have to be large.
Nice to have
• Clear Bright Colours
• I have attached last year's posters to give an idea of what we are interested in.

```html
<!DOCTYPE html>
<html lang="en">
<head>
<meta charset="utf-8">
<title>HALT – Hush And Look Through</title>
<link href="https://fonts.googleapis.com/css2?family=Open+Sans:wght@300;400;700&display=swap" rel="stylesheet">
<style>
  :root {
    --ink-navy: #1b2938;
    --ink-black: #0d0d0d;
    --sky-deep: #3f5f7c;
    --sky-mid: #7f9db5;
    --sky-light: #b7cadb;
    --storm-grey: #8d969e;
    --storm-dark: #5b646c;
    --art-blue: #2f4a74;
    --art-warm: #e8b99a;
    --art-hair: #c9883a;
  }
  html, body {
    margin: 0;
    padding: 0;
    overflow: hidden;
    background: #ffffff;
  }
  .poster {
    position: relative;
    width: 777px;
    height: 1200px;
    overflow: hidden;
    font-family: "Open Sans", Arial, sans-serif;
    background:
      radial-gradient(ellipse 60% 30% at 20% 12%, rgba(183,202,219,0.55), transparent 70%),
      radial-gradient(ellipse 50% 25% at 85% 5%, rgba(40,62,86,0.7), transparent 70%),
      radial-gradient(ellipse 70% 30% at 50% 35%, rgba(183,202,219,0.6), transparent 70%),
      radial-gradient(ellipse 60% 30% at 15% 70%, rgba(91,100,108,0.55), transparent 70%),
      radial-gradient(ellipse 60% 30% at 90% 80%, rgba(91,100,108,0.6), transparent 70%),
      radial-gradient(ellipse 60% 25% at 40% 92%, rgba(190,196,200,0.7), transparent 70%),
      linear-gradient(180deg, var(--sky-deep) 0%, var(--sky-mid) 35%, var(--storm-grey) 70%, var(--storm-dark) 100%);
  }
  .title {
    position: absolute;
    top: 8px;
    left: 0;
    width: 100%;
    margin: 0;
    text-align: center;
    font-weight: 300;
    font-size: 188px;
    line-height: 1;
    letter-spacing: 6px;
    color: var(--ink-navy);
  }
  .subtitle {
    position: absolute;
    top: 192px;
    left: 0;
    width: 100%;
    margin: 0;
    text-align: center;
    font-weight: 300;
    font-size: 62px;
    line-height: 68px;
    color: var(--ink-navy);
  }
  .reading-art {
    position: absolute;
    left: 92px;
    top: 356px;
    width: 592px;
    height: 584px;
    border-radius: 40% 40% 6px 6px;
    background:
      radial-gradient(ellipse 70% 45% at 50% 30%, var(--art-warm), transparent 70%),
      linear-gradient(180deg, var(--art-hair) 0%, var(--art-warm) 40%, var(--art-blue) 60%, var(--art-blue) 100%);
  }
  .date-slot {
    position: absolute;
    top: 962px;
    left: 0;
    width: 100%;
    margin: 0;
    text-align: center;
    font-weight: 700;
    font-size: 74px;
    line-height: 1;
    letter-spacing: -1px;
    color: var(--ink-black);
  }
  .partner {
    position: absolute;
    display: flex;
    align-items: center;
    gap: 10px;
    font-weight: 700;
    font-size: 44px;
    color: var(--ink-black);
  }
  .partner-mark {
    width: 26px;
    height: 26px;
    border-radius: 50%;
    background: var(--ink-black);
  }
  .partner-union {
    left: 26px;
    top: 1100px;
  }
  .partner-association {
    right: 24px;
    top: 1110px;
  }
</style>
</head>
<body>
  <main class="poster">
    <h1 class="title">HALT</h1>
    <p class="subtitle">HUSH AND LOOK<br>THROUGH</p>
    <div class="reading-art" role="img" aria-label="Illustration of five smiling children reading a large blue book together"></div>
    <p class="date-slot">DD.MM.YY</p>
    <div class="partner partner-union"><span class="partner-mark"></span>KEU</div>
    <div class="partner partner-association">HSKA</div>
  </main>
</body>
</html>
```